FRONT BUS CARD:

We were maybe thinking to have the text in a "common seal" which is an oval shape. Or BRIGHTMORE LEDGER underlined, then AUSTRALIA underneath...

Picture to have in the seal, or next to the words if seal not used: Gold Bars (3 of them), or scales of justice..

LOGO and pic and font to be in shiny gold.
We want 1 black background design and 1 white background design.

Logo Text

BRIGHTMORE LEDGER HOLDINGS

```html
<!DOCTYPE html>
<html lang="en">
<head>
<meta charset="utf-8">
<title>Brightmore Ledger Holdings – Business Cards</title>
<link rel="stylesheet" href="https://fonts.googleapis.com/css2?family=Jost:wght@400;500;600&display=swap">
<style>
  :root {
    --backdrop: #e9ecee;
    --card: #ffffff;
    --gold: #c9a227;
    --ink: #2b2b2b;
    --ink-soft: #3a3a3a;
    --shadow: rgba(20, 35, 45, 0.18);
  }
  * { box-sizing: border-box; margin: 0; padding: 0; }
  html, body {
    width: 1200px; height: 960px; overflow: hidden;
    background: var(--backdrop);
    font-family: "Jost", Arial, sans-serif;
  }
  .sheet {
    width: 1200px; height: 960px;
    display: flex; flex-direction: column;
    align-items: center; justify-content: center; gap: 48px;
  }
  .card {
    width: 735px; height: 420px;
    background: var(--card);
    box-shadow: 0 10px 30px var(--shadow);
    display: flex; align-items: center;
  }
  .brand {
    display: flex; flex-direction: column; align-items: center; gap: 18px;
    color: var(--gold); font-weight: 500; text-align: center;
    letter-spacing: 0.08em; text-transform: uppercase;
  }
  .brand-dot {
    width: 34px; height: 34px; border-radius: 50%; background: var(--gold);
  }
  .brand-name { font-size: 30px; line-height: 1.25; }
  /* contact side */
  .card--details { padding: 0 0 0 60px; }
  .card--details .brand { width: 300px; }
  .card--details .brand-name { font-size: 26px; }
  .divider {
    width: 2px; height: 250px; background: var(--gold);
    margin: 0 52px 0 34px;
  }
  .person-name { font-size: 26px; font-weight: 600; color: var(--ink); }
  .person-role { font-size: 24px; font-weight: 400; color: var(--ink-soft); margin-top: 2px; }
  .contact-list { list-style: none; margin-top: 40px; display: grid; gap: 16px; }
  .contact-list li {
    display: flex; align-items: center; gap: 12px;
    font-size: 17px; color: var(--ink-soft);
  }
  .contact-list svg { width: 14px; height: 14px; fill: var(--ink); flex: none; }
  /* logo side */
  .card--brand { justify-content: center; }
</style>
</head>
<body>
<main class="sheet">
  <section class="card card--details" aria-label="Business card, contact side">
    <div class="brand">
      <span class="brand-dot" aria-hidden="true"></span>
      <span class="brand-name">Brightmore Ledger<br>Holdings</span>
    </div>
    <span class="divider" aria-hidden="true"></span>
    <div class="contact">
      <p class="person-name">Daniel Rourke</p>
      <p class="person-role">Director</p>
      <ul class="contact-list">
        <li>
          <svg viewBox="0 0 16 16" aria-hidden="true"><path d="M4 1l3 3-2 2c1 2 3 4 5 5l2-2 3 3-2 3C7 15 1 9 1 3z"/></svg>
          + 61 400 555 218
        </li>
        <li>
          <svg viewBox="0 0 16 16" aria-hidden="true"><path d="M4 0h8v16H4zM6 2v10h4V2z"/></svg>
          + 61 (0)2 5550 1234
        </li>
        <li>
          <svg viewBox="0 0 16 16" aria-hidden="true"><path d="M0 3h16v10H0zM1.5 4.5L8 9l6.5-4.5z"/></svg>
          name@brightmoreledger.com.au
        </li>
        <li>
          <svg viewBox="0 0 16 16" aria-hidden="true"><circle cx="8" cy="8" r="7"/></svg>
          www.brightmoreledger.com.au
        </li>
      </ul>
    </div>
  </section>

  <section class="card card--brand" aria-label="Business card, brand side">
    <div class="brand">
      <span class="brand-dot" aria-hidden="true"></span>
      <span class="brand-name">Brightmore Ledger<br>Holdings</span>
    </div>
  </section>
</main>
</body>
</html>
```